Web Developer Wordpress theme

I'm a web developer but a poor designer so i need somebody to design me a cool and professional WordPress theme. I specialize in shopping cart developments and modifications as well as hosting for these system so would like the design to show this off. I am UK based and want this to also come across in the design.
As for colors and layout i am open mined just use your imaginantion i will let know what i think of your designs.
also forgot to mention my business name is vartelux
and my exsiting site is vartelux.co.uk

```html
<!DOCTYPE html>
<html lang="en">
<head>
<meta charset="utf-8">
<title>Vartelux – UK Freelance Web Developer</title>
<link rel="stylesheet" href="https://fonts.googleapis.com/css2?family=Mulish:ital,wght@0,400;0,700;0,800;1,400;1,700;1,800&family=Arimo:ital,wght@0,400;0,700;1,400;1,700&display=swap">
<style>
:root{
  --navy-deep:#0b1c3c;
  --navy:#0d2d5e;
  --navy-mid:#164a86;
  --strip:#1b2244;
  --orange:#ff8a00;
  --orange-light:#ffa43a;
  --sky:#1aa0e8;
  --coral:#ee5a3c;
  --ink:#1c2230;
  --text:#333a44;
  --footer-bg:#e7f1fb;
  --bar:#13203f;
  --white:#ffffff;
  --card:#eef1f4;
  --tag:#222428;
  --red-btn:#d9141b;
  --blue-btn:#1d6fd6;
}
*{margin:0;padding:0;box-sizing:border-box}
html,body{width:1117px;height:1200px;overflow:hidden;background:var(--white)}
body{font-family:"Arimo",Arial,sans-serif;color:var(--text)}
.page{position:relative;width:1117px;height:1200px;overflow:hidden}
.abs{position:absolute}

/* header */
.hero{left:0;top:0;width:1117px;height:561px;
  background:radial-gradient(ellipse 600px 260px at 900px 380px,#1f63b0 0%,rgba(31,99,176,0) 70%),
  linear-gradient(180deg,var(--navy-deep) 0%,var(--navy) 30%,var(--navy-mid) 75%,#123e74 100%)}
.util-nav{left:450px;top:13px;display:flex;font-size:12.5px;color:#3aa6ef}
.util-nav span{padding:0 12px;border-left:1px solid #2f6fae;line-height:14px}
.util-nav span:first-child{border-left:none}
.search{left:825px;top:4px;width:274px;height:25px;display:flex}
.search .field{width:202px;height:100%;background:var(--white)}
.search .btn{flex:1;background:#0f3768;color:var(--white);font-size:12.5px;text-align:center;line-height:25px}
.brand{left:56px;top:30px;display:flex;align-items:center;gap:12px}
.brand .dot{width:46px;height:46px;border-radius:50%;background:var(--sky)}
.brand .name{font-family:"Mulish",sans-serif;font-weight:800;font-size:58px;color:var(--orange);letter-spacing:-1px;line-height:1}
.tagline{left:150px;top:104px;font-size:11.5px;letter-spacing:3px;color:#7b93b4}
.main-nav{left:421px;top:76px;display:flex;align-items:center;font-size:16px;color:var(--white)}
.main-nav span{padding:0 22px;line-height:31px}
.main-nav .active{background:#0a2a52;border-radius:8px;color:#55b7ff;box-shadow:inset 0 1px 2px rgba(0,0,0,.5);padding:0 22px}
.hero-title{left:67px;top:172px;font-family:"Mulish",sans-serif;font-weight:800;font-size:36px;color:var(--orange)}
.hero-sub{left:67px;top:226px;width:680px;font-size:20.5px;line-height:24px;font-style:italic;color:var(--sky)}
.hero-text{left:70px;top:308px;width:500px;font-size:15.5px;line-height:19px;color:var(--white)}
.cta{top:392px;height:34px;width:131px;border-radius:4px;text-align:center;line-height:34px;font-size:15.5px;color:#10213d}
.cta.read{left:69px;background:linear-gradient(#ffb347,#ff8400)}
.cta.try{left:216px;background:linear-gradient(#5ab0ff,#1e6fd8);color:#0b1c3c}
.product-art{left:748px;top:257px;width:296px;height:234px;border-radius:4px;
  background:linear-gradient(135deg,#f39a1e 0%,#2a2a2a 45%,#1a1a1a 75%,#e08a16 100%);opacity:.92}
.strip{left:0;top:472px;width:1117px;height:89px;background:linear-gradient(180deg,#252b4e,var(--strip))}
.feature{top:493px;display:flex;gap:12px}
.feature .icon{width:42px;height:42px;border-radius:50%;background:linear-gradient(#eaf5ff,#9cc6ea);display:flex;align-items:center;justify-content:center}
.feature .title{font-weight:700;font-style:italic;font-size:16px;color:var(--white);line-height:20px}
.feature .sub{font-size:13.5px;color:var(--orange);line-height:20px}
.feature .sub svg{margin-left:10px;vertical-align:-1px}

/* content */
.sec-head{top:597px;font-family:"Mulish",sans-serif;font-style:italic;font-weight:700;font-size:27px;color:var(--coral)}
.services{left:70px;top:646px;list-style:none}
.services li{height:33.5px;font-weight:700;font-style:italic;font-size:14px;color:var(--ink);display:flex;align-items:center;gap:7px}
.services li::before{content:"";width:11px;height:11px;border-radius:50%;background:var(--coral);box-shadow:0 0 0 2px #fbd3c9}
.about{left:362px;top:645px;width:310px;font-size:13.8px;line-height:20px;color:var(--text)}
.about p+p{margin-top:20px}
.card{left:792px;width:286px;height:84px;background:linear-gradient(#fafbfc,var(--card));border-radius:4px;border:1px solid #dfe3e7;padding:6px 12px}
.card h3{font-style:italic;font-weight:700;font-size:15.5px;color:var(--ink)}
.card p{margin-top:8px;width:200px;font-size:12.3px;line-height:14px;color:#4a505a}
.price{left:1007px;width:84px;border-radius:5px;background:linear-gradient(#3a3d42,var(--tag));color:var(--white);text-align:center;overflow:hidden}
.price .amt{font-family:"Mulish",sans-serif;font-weight:800;font-size:27px;margin-top:14px;line-height:28px}
.price .from{font-weight:700;font-size:13px;line-height:16px}
.price .order{position:absolute;left:0;bottom:0;width:100%;height:24px;font-size:11px;font-weight:700;line-height:24px;letter-spacing:.5px}
.price .order.red{background:var(--red-btn)}
.price .order.blue{background:var(--blue-btn)}

/* footer */
.footer{left:0;top:947px;width:1117px;height:224px;background:var(--footer-bg)}
.controls{top:975px}
.controls h4{font-family:"Mulish",sans-serif;font-style:italic;font-weight:400;font-size:16px;color:#111;margin-bottom:10px}
.controls ul{list-style:none;padding-left:7px}
.controls li{font-size:12.5px;line-height:20px;color:#222}
.testimonial{left:785px;top:963px;width:312px}
.testimonial h4{font-style:italic;font-weight:700;font-size:15.5px;color:#111;margin-bottom:8px}
.testimonial blockquote{font-size:12px;line-height:20px;color:#222}
.testimonial cite{display:block;text-align:right;margin-top:8px;font-style:italic;font-weight:700;font-size:12.5px;color:#111}
.social{left:589px;top:1096px;display:flex;gap:19px}
.social span{width:41px;height:41px;border-radius:50%;box-shadow:0 2px 3px rgba(0,0,0,.3);border:2px solid var(--white)}
.social .s1{background:#c4121a}
.social .s2{background:#2a5aa8}
.social .s3{background:#3aa6dd}
.bottom-bar{left:0;top:1171px;width:1117px;height:29px;background:var(--bar);font-size:12.5px;color:#3aa6ef;line-height:29px;padding-left:16px}
</style>
</head>
<body>
<div class="page">
  <header class="abs hero"></header>
  <nav class="abs util-nav"><span>Blog</span><span>Support</span><span>FAQ</span><span>Contacts</span><span>Sitemap</span></nav>
  <div class="abs search"><div class="field"></div><div class="btn">Search</div></div>
  <div class="abs brand"><span class="dot"></span><span class="name">Vartelux</span></div>
  <div class="abs tagline">serious web development</div>
  <nav class="abs main-nav"><span class="active">Home</span><span>About us</span><span>Services</span><span>Addons</span><span>Our E-commerce Hosting</span></nav>

  <h1 class="abs hero-title">UK Freelance Web Developer</h1>
  <p class="abs hero-sub">Freelance web developer avaliable for hire, Specializing in Cartwell shopping cart and creating addons and customized templates.</p>
  <p class="abs hero-text">I have been a freelance developer for over 5 years now and complete all sizes of projects starting out on CodeHire doing small project then going on to the larger projects.</p>
  <div class="abs cta read">Read more</div>
  <div class="abs cta try">Try it now</div>
  <div class="abs product-art" role="img" aria-label="Three boxed software packages for the out of stock notification addon"></div>

  <div class="abs strip"></div>
  <div class="abs feature" style="left:65px">
    <div class="icon"><svg width="24" height="20" viewBox="0 0 24 20"><path d="M1 2h4l3 11h12l3-8H7" fill="none" stroke="#1b2244" stroke-width="2"/><circle cx="10" cy="17" r="2" fill="#1b2244"/><circle cx="18" cy="17" r="2" fill="#1b2244"/></svg></div>
    <div><div class="title">Shopping cart&nbsp; Addons</div><div class="sub">just need a few extra features<svg width="9" height="11"><path d="M0 0l9 5.5L0 11z" fill="#fff"/></svg></div></div>
  </div>
  <div class="abs feature" style="left:345px">
    <div class="icon"><svg width="20" height="20" viewBox="0 0 20 20" fill="#1b2244"><rect x="0" y="0" width="5" height="5"/><rect x="7.5" y="0" width="5" height="5"/><rect x="15" y="0" width="5" height="5"/><rect x="0" y="7.5" width="5" height="5"/><rect x="7.5" y="7.5" width="5" height="5"/><rect x="15" y="7.5" width="5" height="5"/><rect x="0" y="15" width="5" height="5"/><rect x="7.5" y="15" width="5" height="5"/><rect x="15" y="15" width="5" height="5"/></svg></div>
    <div><div class="title">Shopping cart&nbsp; Addons</div><div class="sub">give your site a revamp<svg width="9" height="11"><path d="M0 0l9 5.5L0 11z" fill="#fff"/></svg></div></div>
  </div>
  <div class="abs feature" style="left:626px">
    <div class="icon"><svg width="24" height="22" viewBox="0 0 24 22"><path d="M12 1l11 5-11 5L1 6z" fill="#f08a1c"/><path d="M1 11l11 5 11-5" fill="none" stroke="#e24a2a" stroke-width="3"/><path d="M1 16l11 5 11-5" fill="none" stroke="#2a78c8" stroke-width="3"/></svg></div>
    <div><div class="title">Shopping cart&nbsp; Addons</div><div class="sub">Your current host just not up to your<svg width="9" height="11"><path d="M0 0l9 5.5L0 11z" fill="#fff"/></svg></div></div>
  </div>

  <h2 class="abs sec-head" style="left:70px">Services</h2>
  <ul class="abs services">
    <li>Shopping cart Addons</li><li>Shopping cart Templates</li><li>Shopping cart Software</li><li>Shopping cart Hosting</li>
    <li>Shopping cart Addons</li><li>Shopping cart Templates</li><li>Shopping cart Software</li><li>Shopping cart Hosting</li>
  </ul>

  <h2 class="abs sec-head" style="left:362px">Who we are?</h2>
  <div class="abs about">
    <p>Vartelux, is a freelance web developer specializing in online shopping cart solution whether it is just a simple PayBridge cart or a full blown shopping management system we customize and style it to your requirements.</p>
    <p>Vartelux, is a freelance web developer specializing in online shopping cart solution whether it is just a simple PayBridge cart or a full blown shopping management system we customize and style it to your requirements.</p>
  </div>

  <h2 class="abs sec-head" style="left:787px">Our Products</h2>
  <div class="abs card" style="top:655px"><h3>Cartwell Addons</h3><p>We create addon and modules to work with the cartwell shopping cart system.</p></div>
  <div class="abs price" style="top:631px;height:103px"><div class="amt">£90*</div><div class="from">*From</div><div class="order red">ORDER NOW!</div></div>
  <div class="abs card" style="top:790px"><h3>Cartwell Templates</h3><p>So you have the best shopping cart software Now you just need it</p></div>
  <div class="abs price" style="top:766px;height:103px"><div class="amt">£90*</div><div class="from">*From</div><div class="order blue">ORDER NOW!</div></div>

  <footer class="abs footer"></footer>
  <div class="abs controls" style="left:83px"><h4>Controls</h4><ul><li>Log in</li><li>Entries RSS</li><li>Comments RSS</li><li>BlogPress.org</li></ul></div>
  <div class="abs controls" style="left:296px"><h4>Controls</h4><ul><li>Log in</li><li>Entries RSS</li><li>Comments RSS</li><li>BlogPress.org</li></ul></div>
  <div class="abs controls" style="left:521px"><h4>Controls</h4><ul><li>Log in</li><li>Entries RSS</li><li>Comments RSS</li><li>BlogPress.org</li></ul></div>
  <div class="abs testimonial">
    <h4>Our Customers say</h4>
    <blockquote>“ carried out what we thought was a complex piece of scripting on our Cartwell website He completed the work quickly, well within agreed timescales - it was accurate and most importantly on agreed budget. We intend to use his skills for all future development on the site and he comes highly recommended by Quick Quizpoint Many thanks “</blockquote>
    <cite>Mark Hale, www.quick-quizpoint.co.uk</cite>
  </div>
  <div class="abs social"><span class="s1"></span><span class="s2"></span><span class="s3"></span></div>
  <div class="abs bottom-bar">Website content Copyrighted Vartelux 2011</div>
</div>
</body>
</html>
```